Harwick Structure Works needs a Business card design and logo

We Need a business card design and logo for a Building & Construction business based in Melbourne. We work in both the Domestic & Commercial sector. We specialize in all aspects of building including extensions, Renovations, and alterations. Construction Management, Project Management, And labour hire

Industry/Entity Type

Business

```html
<!DOCTYPE html>
<html lang="en">
<head>
<meta charset="UTF-8">
<title>Harwick Structure Works – Business Card</title>
<link href="https://fonts.googleapis.com/css2?family=Exo+2:wght@400;600;700&display=swap" rel="stylesheet">
<style>
  :root {
    --bg: #8e8f91;
    --card-white: #ffffff;
    --green-dark: #1f9a3c;
    --green-light: #6ec13b;
    --swoosh-dark: #3a3a3a;
    --swoosh-light: #9a9a9a;
    --ink-dark: #0e3a16;
    --brand-ink: #4a4a4a;
    --brand-mark: #3fae3a;
  }
  * { margin: 0; padding: 0; box-sizing: border-box; }
  html, body {
    width: 1200px; height: 771px; overflow: hidden;
    background: var(--bg);
    font-family: "Exo 2", sans-serif;
  }
  .canvas {
    position: relative; width: 1200px; height: 771px;
    display: flex; align-items: center; justify-content: center; gap: 40px;
  }
  .card {
    position: relative; width: 540px; height: 309px;
    background: var(--card-white);
    box-shadow: 0 6px 18px rgba(0,0,0,0.25);
    overflow: hidden;
  }
  .card-art { position: absolute; inset: 0; width: 100%; height: 100%; }

  .contact {
    position: absolute; left: 30px; top: 30px;
    color: var(--ink-dark);
  }
  .contact-name {
    font-size: 21px; font-weight: 700; letter-spacing: 1.5px;
    text-transform: uppercase;
  }
  .contact-role { font-size: 13px; margin-top: 2px; }
  .contact-address { font-size: 13px; margin-top: 18px; line-height: 1.35; }
  .contact-list { list-style: none; margin-top: 14px; font-size: 12.5px; }
  .contact-list li { display: flex; align-items: center; gap: 8px; height: 20px; }
  .contact-list svg { width: 13px; height: 13px; fill: var(--ink-dark); flex: none; }

  .brand {
    position: absolute; display: flex; align-items: center; gap: 10px;
    color: var(--brand-ink); font-weight: 600; letter-spacing: 0.5px;
    white-space: nowrap;
  }
  .brand-mark { background: var(--brand-mark); flex: none; }
  .card-front .brand {
    left: 380px; top: 150px; width: 145px;
    flex-direction: column; gap: 8px;
    font-size: 15px; line-height: 1.25; text-align: center;
    white-space: normal;
  }
  .card-front .brand-mark { width: 14px; height: 14px; }
  .card-back .brand { left: 50%; top: 50%; transform: translate(-50%, -50%); font-size: 26px; gap: 14px; }
  .card-back .brand-mark { width: 20px; height: 20px; }
</style>
</head>
<body>
<main class="canvas">

  <section class="card card-front" aria-label="Business card front">
    <svg class="card-art" viewBox="0 0 540 309" aria-hidden="true">
      <defs>
        <linearGradient id="greenPanel" x1="0" y1="1" x2="1" y2="0">
          <stop offset="0" stop-color="var(--green-dark)"/>
          <stop offset="1" stop-color="var(--green-light)"/>
        </linearGradient>
        <linearGradient id="swoosh" x1="0" y1="0" x2="0" y2="1">
          <stop offset="0" stop-color="var(--swoosh-dark)"/>
          <stop offset="1" stop-color="var(--swoosh-light)" stop-opacity="0.3"/>
        </linearGradient>
      </defs>
      <path d="M0,0 H405 C350,70 305,190 300,309 H0 Z" fill="url(#greenPanel)"/>
      <path d="M418,0 C362,72 318,190 312,309 L318,309 C326,195 372,82 432,0 Z" fill="url(#swoosh)"/>
    </svg>

    <div class="contact">
      <p class="contact-name">Owen Marlow</p>
      <p class="contact-role">Managing Director</p>
      <p class="contact-address">27 Keel Street, Level 4<br>Dockside Road VIC</p>
      <ul class="contact-list">
        <li><svg viewBox="0 0 16 16"><path d="M3 1h3l1.5 4-2 1.3a9 9 0 0 0 4.2 4.2L11 8.5l4 1.5v3a2 2 0 0 1-2 2A12 12 0 0 1 1 3a2 2 0 0 1 2-2z"/></svg>012 345 6789</li>
        <li><svg viewBox="0 0 16 16"><path d="M4 1h8v4H4zM1 6h14v7h-3v2H4v-2H1zM5 10v4h6v-4z"/></svg>012 345 6789</li>
        <li><svg viewBox="0 0 16 16"><path d="M4 0h8a1 1 0 0 1 1 1v14a1 1 0 0 1-1 1H4a1 1 0 0 1-1-1V1a1 1 0 0 1 1-1zm1 2v10h6V2zm3 11a1 1 0 1 0 0 2 1 1 0 0 0 0-2z"/></svg>012 345 6789</li>
        <li><svg viewBox="0 0 16 16"><path d="M1 3h14v10H1zm1.5 1.2L8 8.5l5.5-4.3z"/></svg>hello@harwickworks.com</li>
        <li><svg viewBox="0 0 16 16"><path d="M8 0a8 8 0 1 0 0 16A8 8 0 0 0 8 0zm0 2a6 6 0 1 1 0 12A6 6 0 0 1 8 2zm0 2a4 4 0 1 0 0 8 4 4 0 0 0 0-8z"/></svg>www.harwickworks.com</li>
      </ul>
    </div>

    <div class="brand"><span class="brand-mark"></span>Harwick Structure Works</div>
  </section>

  <section class="card card-back" aria-label="Business card back">
    <div class="brand"><span class="brand-mark"></span>Harwick Structure Works</div>
  </section>

</main>
</body>
</html>
```